Cleaning services Business Card Design

I need a business card design for my Cleaning business. I would like perhaps emphasis on the company name, Muddle to Marvel. Maybe the Muddle would to dirty and the marvel would have sprinkles.

Industry/Entity Type

Business

Contact Information for Business Card

Muddle to Marvel Cleaning Services, Teodoro Perlas, Industrial, Commercial, & Residential 418-635-0247

```html
<!DOCTYPE html>
<html lang="en">
<head>
<meta charset="utf-8">
<title>Muddle to Marvel Cleaning Services – Business Card</title>
<link rel="stylesheet" href="https://fonts.googleapis.com/css2?family=Oswald:wght@500;600&family=Open+Sans:wght@400;600&display=swap">
<style>
  :root {
    --backdrop: #3a302c;
    --card: #141414;
    --card-edge: #222;
    --silver: #cfd3d7;
    --blue: #1e8fe6;
    --white: #eceff1;
    --divider: #6d6d6d;
  }
  * { box-sizing: border-box; margin: 0; padding: 0; }
  html, body { width: 1200px; height: 814px; overflow: hidden; }
  body {
    background: var(--backdrop);
    position: relative;
    font-family: "Open Sans", Arial, sans-serif;
  }
  .card {
    position: absolute;
    top: 258px;
    width: 520px;
    height: 297px;
    background: var(--card);
    border: 1px solid var(--card-edge);
    border-radius: 3px;
    box-shadow: 0 8px 24px rgba(0,0,0,.35);
    overflow: hidden;
  }
  .card--front { left: 60px; }
  .card--back { left: 620px; }

  .wordmark {
    font-family: "Oswald", Arial, sans-serif;
    font-weight: 600;
    color: var(--silver);
    text-transform: uppercase;
    line-height: 1;
    display: flex;
    align-items: flex-start;
    gap: 8px;
  }
  .wordmark__text { display: block; }
  .wordmark__name { display: block; font-size: 40px; letter-spacing: 1px; }
  .wordmark__sub { display: block; font-size: 13px; letter-spacing: 8.2px; margin-top: 4px; }
  .wordmark__dot {
    width: 8px; height: 8px; border-radius: 50%;
    background: var(--silver); margin-top: 2px;
  }

  .card--front .wordmark { position: absolute; left: 100px; top: 92px; }
  .tagline {
    position: absolute; left: 0; right: 0; top: 196px;
    text-align: center;
    font-family: "Oswald", Arial, sans-serif;
    font-weight: 500;
    font-size: 17px;
    letter-spacing: .4px;
    color: var(--blue);
  }

  .card--back .wordmark { position: absolute; left: 24px; top: 116px; gap: 6px; }
  .card--back .wordmark__name { font-size: 27px; letter-spacing: .6px; }
  .card--back .wordmark__sub { font-size: 9px; letter-spacing: 5.6px; margin-top: 3px; }
  .card--back .wordmark__dot { width: 6px; height: 6px; }
  .divider {
    position: absolute; left: 286px; top: 74px;
    width: 1px; height: 150px;
    background: linear-gradient(to bottom, transparent, var(--divider) 30%, var(--divider) 70%, transparent);
  }
  .contact { position: absolute; left: 304px; top: 94px; color: var(--white); }
  .contact__name {
    font-size: 18px; font-weight: 600; color: var(--blue);
    text-transform: uppercase; letter-spacing: .5px; line-height: 1.3;
  }
  .contact__role { font-size: 13.5px; margin-bottom: 8px; }
  .contact__list { list-style: none; font-size: 13.5px; }
  .contact__list li { display: flex; align-items: center; gap: 8px; height: 22px; }
  .contact__list svg { width: 13px; height: 13px; fill: var(--blue); flex: none; }
</style>
</head>
<body>
  <section class="card card--front" aria-label="Card front">
    <div class="wordmark">
      <span class="wordmark__text">
        <span class="wordmark__name">Muddle to Marvel</span>
        <span class="wordmark__sub">Cleaning Services</span>
      </span>
      <span class="wordmark__dot"></span>
    </div>
    <p class="tagline">Industrial, Commercial, &amp; Residential</p>
  </section>

  <section class="card card--back" aria-label="Card back">
    <div class="wordmark">
      <span class="wordmark__text">
        <span class="wordmark__name">Muddle to Marvel</span>
        <span class="wordmark__sub">Cleaning Services</span>
      </span>
      <span class="wordmark__dot"></span>
    </div>
    <div class="divider"></div>
    <div class="contact">
      <p class="contact__name">Teodoro Perlas</p>
      <p class="contact__role">CEO/Founder</p>
      <ul class="contact__list">
        <li>
          <svg viewBox="0 0 24 24" aria-hidden="true"><path d="M6.6 10.8a15.1 15.1 0 0 0 6.6 6.6l2.2-2.2a1 1 0 0 1 1-.25 11.4 11.4 0 0 0 3.6.57 1 1 0 0 1 1 1V20a1 1 0 0 1-1 1A17 17 0 0 1 3 4a1 1 0 0 1 1-1h3.5a1 1 0 0 1 1 1c0 1.25.2 2.45.57 3.57a1 1 0 0 1-.25 1z"/></svg>
          418-635-0247
        </li>
        <li>
          <svg viewBox="0 0 24 24" aria-hidden="true"><path d="M2 5h20v2l-10 7L2 7z"/><path d="M2 9l10 7 10-7v10H2z"/></svg>
          hello@muddlemarvel.com
        </li>
        <li>
          <svg viewBox="0 0 24 24" aria-hidden="true"><path d="M12 2a10 10 0 1 0 0 20 10 10 0 0 0 0-20zm-1 17.9A8 8 0 0 1 4.1 11H7a15 15 0 0 0 4 8.9zM7 9H4.6A8 8 0 0 1 11 4.1 15 15 0 0 0 7 9zm6 10.9A15 15 0 0 0 17 13h2.9a8 8 0 0 1-6.9 6.9zM17 11a15 15 0 0 0-4-6.9A8 8 0 0 1 19.9 11z"/></svg>
          www.muddlemarvel.com
        </li>
      </ul>
    </div>
  </section>
</body>
</html>
```